Web design and coding for Harbor Lantern

We are a consultancy specialising in contact centre services. Our target audience is organisations who have inhouse contact centres, outsource contact centre services and require services such as knowledge management, advisory, workforce management and training/OD.

Our purpose is 'We create customer experience heroes' and our tagline is 'Creating customer experience heroes'. Our vision "Asia Pacific's most Trusted Advisor in Customer Experience and Service Operations"

We need a website refresh - one that appeals to our target audience , captures our purpose and as well as our purpose. The website would support our marketing and direct sales and imagery should reflect our purpose, vision and appeal to our target market.

The website needs to be able to showcase our team (profiles) and case studies with the option of posting videos / articles /newsletters as well. Potential for capturing customer details would also be considered.
There may be some other ideas you have which we would also be open to.
Logo should remain as is (see Messaging House). Values are internal .

We will need the ability to update the website (using Wordpress) so design should cater for this.
Updates

Hi All Thanks for your submissions - we are reviewing designs early next week.

Hi Designers Thank you for your submissions. We've had a little delay due to COVID 19 work restrictions in selecting the design. We are hoping to make a decision by the end of the month. I'm sorry for the delay and will keep you updated. Thank you!

Target Market(s)

Asia Pac Business decision makers with Contact Centres - COOs, Knowledge Managers, Head of of L&D, Head of Workforce, GM Operations

Coding

Coded - Design and coding required

Number of Pages Required

5+ page

Colors
34a7d8
85acd3

Requirements
Must have
• See messaging house - HL colours should be used.
Nice to have
• Area for case studies and bios
Area for newsletters / posts
Should not have
• Values are internal - this gives the feel of the company rather than needing to be promoted.

```html
<!DOCTYPE html>
<html lang="en">
<head>
<meta charset="utf-8">
<title>Harbor Lantern — Creating customer experience heroes</title>
<link rel="stylesheet" href="https://fonts.googleapis.com/css2?family=Fira+Sans:wght@400;500;600;700&display=swap">
<style>
:root{
  --blue:#2e8fd8;
  --blue-dark:#1f7cc4;
  --pill:#6f9bd1;
  --ink:#1c1c1c;
  --text:#333;
  --muted:#666;
  --rule:#a9a9a9;
  --soft:#f4f1f1;
  --footer:#1b1b1c;
  --white:#fff;
}
*{margin:0;padding:0;box-sizing:border-box}
html,body{width:1200px;height:3524px;overflow:hidden}
body{font-family:"Fira Sans",Arial,sans-serif;color:var(--text);background:var(--white);position:relative}
.abs{position:absolute}
.btn{position:absolute;display:flex;align-items:center;justify-content:center;border-radius:30px;background:var(--blue);color:var(--white);font-weight:600;text-transform:uppercase;letter-spacing:.3px}
.section-title{position:absolute;left:0;width:1200px;text-align:center;font-size:27px;font-weight:700;color:var(--ink);letter-spacing:.5px}
.title-rule{position:absolute;left:578px;width:44px;height:4px;background:var(--rule);border-radius:2px}

/* header */
.brand{position:absolute;display:flex;align-items:center;gap:10px;font-weight:700;color:var(--blue)}
.brand-dot{border-radius:50%;background:var(--blue)}
.contact-item{position:absolute;display:flex;gap:12px;align-items:flex-start}
.contact-icon{width:30px;height:30px;border-radius:50%;background:var(--blue);display:flex;align-items:center;justify-content:center;margin-top:8px}
.contact-label{font-size:15px;color:#444;letter-spacing:.3px}
.contact-value{font-size:17px;color:var(--ink);font-weight:500;margin-top:4px}
.contact-value.big{font-size:22px}
.nav{position:absolute;top:98px;left:518px;display:flex;gap:0;font-size:15.5px;color:var(--ink);letter-spacing:.3px}
.nav span{margin-right:35px}
.nav .active{color:var(--blue);text-decoration:underline;text-underline-offset:4px}

/* hero */
.hero{position:absolute;top:141px;left:0;width:1200px;height:538px;background:linear-gradient(180deg,#dfe9f1 0%,#c8d6e2 40%,#9fb2c1 70%,#6f7a82 100%)}
.hero-title{position:absolute;left:579px;top:46px;font-size:32px;font-weight:600;line-height:38px;color:var(--ink);letter-spacing:.5px}
.hero-sub{position:absolute;left:579px;top:138px;font-size:15px;color:#333;letter-spacing:.3px}
.slider-arrow{position:absolute;top:252px;width:36px;height:36px;background:#2a2a2a;display:flex;align-items:center;justify-content:center}

/* services */
.service{position:absolute;top:806px;width:226px;height:392px;border-radius:113px;background:var(--pill);color:var(--white);text-align:center}
.service.dark{background:linear-gradient(180deg,#3b3b3d,#151516)}
.service-icon{position:absolute;left:65px;top:28px;width:96px;height:96px;border-radius:50%;background:var(--white);display:flex;align-items:center;justify-content:center}
.service-name{position:absolute;left:10px;right:10px;top:144px;font-size:15px;font-weight:500;line-height:21px;letter-spacing:.4px}
.service-copy{position:absolute;left:26px;right:26px;top:224px;font-size:13px;line-height:18px;opacity:.92}
.service .btn{left:69px;top:328px;width:88px;height:28px;background:var(--white);color:var(--pill);font-size:11px}
.service.dark .btn{background:var(--blue);color:var(--white)}

/* welcome */
.welcome{position:absolute;top:1256px;left:0;width:1200px;height:406px;background:var(--soft)}
.welcome-photo{position:absolute;left:0;top:0;width:380px;height:406px;background:linear-gradient(90deg,#c9b6ab 0%,#d8cfc9 60%,rgba(244,241,241,0) 100%)}
.welcome-kicker{position:absolute;left:625px;top:52px;font-size:19px;color:var(--ink);letter-spacing:.3px}
.welcome-title{position:absolute;left:625px;top:78px;font-size:30px;font-weight:600;color:var(--ink);letter-spacing:.6px}
.welcome-rule{position:absolute;left:625px;top:130px;width:44px;height:4px;background:var(--rule);border-radius:2px}
.welcome-copy{position:absolute;left:625px;top:170px;width:470px;font-size:18.5px;line-height:29px;color:var(--ink)}

/* vision */
.vision{position:absolute;top:1662px;left:0;width:1200px;height:166px;background:linear-gradient(90deg,#2b8ad2,#3595db 50%,#2b8ad2)}
.vision-tag{position:absolute;left:540px;top:38px;width:120px;height:40px;border:2px solid var(--white);border-radius:22px;color:var(--white);font-size:14px;font-weight:600;display:flex;align-items:center;justify-content:center;letter-spacing:.4px}
.vision-text{position:absolute;left:0;width:1200px;top:102px;text-align:center;color:var(--white);font-size:17.5px;font-weight:600;letter-spacing:.5px}

/* team */
.member{position:absolute;top:1960px;width:224px;height:346px;border:2px solid #ddd;border-radius:4px;background:var(--white);text-align:center}
.member-photo{position:absolute;left:0;top:0;width:220px;height:174px;background:linear-gradient(180deg,#b9b6b2,#8a8580)}
.member-name{position:absolute;left:0;right:0;top:200px;font-size:15px;font-weight:600;color:var(--ink);letter-spacing:.4px}
.member-role{position:absolute;left:0;right:0;top:224px;font-size:13px;color:var(--muted)}
.member-copy{position:absolute;left:26px;right:26px;top:258px;font-size:13px;line-height:18px;color:#444}
.member .btn{left:67px;top:329px;width:88px;height:30px;font-size:11.5px}
.team-arrow{position:absolute;top:2122px;width:26px;height:26px;border:1.5px solid #999;border-radius:50%;display:flex;align-items:center;justify-content:center;background:var(--white)}

/* case studies */
.cases{position:absolute;top:2380px;left:0;width:1200px;height:550px;background:linear-gradient(180deg,#f3f3f3,#eeeded)}
.case{position:absolute;top:126px;width:296px;height:378px;background:var(--white)}
.case-media{position:absolute;left:0;top:0;width:296px;height:192px;background:linear-gradient(135deg,#d9d2cc,#8e8580)}
.case-media.night{background:linear-gradient(135deg,#2a3340,#0e141d)}
.play{position:absolute;left:124px;top:72px;width:48px;height:48px;border-radius:50%;background:var(--white);border:4px solid var(--blue);display:flex;align-items:center;justify-content:center}
.case-title{position:absolute;left:25px;right:20px;top:218px;font-size:14px;font-weight:600;line-height:20px;color:var(--ink);letter-spacing:.3px}
.case-copy{position:absolute;left:25px;right:20px;top:272px;font-size:13.5px;line-height:20px;color:#444}
.case .btn{left:30px;top:330px;width:88px;height:28px;font-size:11px}

/* newsletter */
.newsletter{position:absolute;top:2930px;left:0;width:1200px;height:238px;background:linear-gradient(90deg,#3397dd,#2c8ad4)}
.news-title{position:absolute;left:130px;top:66px;font-size:25px;font-weight:600;color:var(--white);letter-spacing:.4px}
.news-copy{position:absolute;left:130px;top:112px;width:320px;font-size:15.5px;line-height:26px;color:#e8f3fb}
.field{position:absolute;left:691px;width:373px;border-bottom:2px solid var(--white);color:var(--white);font-size:14.5px;padding-bottom:6px}
.newsletter .btn{left:691px;top:152px;width:127px;height:40px;background:var(--white);color:var(--blue);font-size:15px}

/* footer */
.footer{position:absolute;top:3168px;left:0;width:1200px;height:356px;background:var(--footer);color:#ddd}
.foot-head{position:absolute;top:52px;font-size:13px;font-weight:600;color:var(--white);letter-spacing:.4px}
.foot-menu{position:absolute;left:488px;top:88px;font-size:12.5px;line-height:20px;color:#ddd}
.foot-item{position:absolute;display:flex;gap:12px;font-size:12px;line-height:16px;color:#ddd}
.foot-icon{width:22px;height:22px;border-radius:50%;background:var(--white);flex:none;margin-top:5px;display:flex;align-items:center;justify-content:center}
.foot-rule{position:absolute;left:131px;top:270px;width:938px;height:1px;background:#333}
.copyright{position:absolute;left:0;width:1200px;top:310px;text-align:center;font-size:10px;color:#ccc}
</style>
</head>
<body>

<!-- Header -->
<header>
  <div class="brand" style="left:131px;top:38px;font-size:26px">
    <span class="brand-dot" style="width:26px;height:26px"></span>Harbor Lantern
  </div>
  <div class="contact-item" style="left:577px;top:25px">
    <div class="contact-icon"><svg width="14" height="10" viewBox="0 0 14 10"><rect x="0.5" y="0.5" width="13" height="9" fill="none" stroke="#fff"/><path d="M1 1l6 5 6-5" fill="none" stroke="#fff"/></svg></div>
    <div><div class="contact-label">E MAILL US</div><div class="contact-value">info@harborlantern.com</div></div>
  </div>
  <div class="contact-item" style="left:877px;top:25px">
    <div class="contact-icon"><svg width="14" height="14" viewBox="0 0 24 24"><path d="M6.6 10.8a15 15 0 006.6 6.6l2.2-2.2c.3-.3.7-.4 1-.2 1.1.4 2.3.6 3.6.6.6 0 1 .4 1 1V20c0 .6-.4 1-1 1A17 17 0 013 4c0-.6.4-1 1-1h3.5c.6 0 1 .4 1 1 0 1.3.2 2.5.6 3.6.1.3 0 .7-.2 1z" fill="#fff"/></svg></div>
    <div><div class="contact-label">CALL US</div><div class="contact-value big">555.010.2040</div></div>
  </div>
  <nav class="nav"><span class="active">HOME</span><span>ABOUT US</span><span>SERVICES</span><span>CASE STUDIES</span><span>CONTACT US</span></nav>
</header>

<!-- Hero -->
<section class="hero" role="img" aria-label="Businessman standing on a rocky summit overlooking a sunlit city skyline">
  <h1 class="hero-title">WE CREATE CUSTOMER<br>EXPERIENCE HEROES</h1>
  <p class="hero-sub">LOREM IPSUM IS SIMPLY DUMMY TEXT OF THE PRINTING</p>
  <div class="btn" style="left:579px;top:182px;width:142px;height:42px;font-size:16px">Read More</div>
  <div class="slider-arrow" style="left:0"><svg width="10" height="14" viewBox="0 0 10 14"><path d="M8 1L2 7l6 6" fill="none" stroke="#fff" stroke-width="2"/></svg></div>
  <div class="slider-arrow" style="left:1164px"><svg width="10" height="14" viewBox="0 0 10 14"><path d="M2 1l6 6-6 6" fill="none" stroke="#fff" stroke-width="2"/></svg></div>
</section>

<!-- Services -->
<h2 class="section-title" style="top:717px">OUR SERVICES</h2>
<div class="title-rule" style="top:766px"></div>

<article class="service" style="left:131px">
  <div class="service-icon"><svg width="54" height="54" viewBox="0 0 54 54"><circle cx="27" cy="22" r="14" fill="var(--pill)"/><rect x="19" y="34" width="16" height="12" fill="var(--pill)"/><path d="M12 24a15 15 0 0130 0" fill="none" stroke="var(--pill)" stroke-width="3"/><circle cx="20" cy="38" r="3" fill="var(--pill)"/></svg></div>
  <div class="service-name">CUSTOMER<br>MANAGEMENT<br>CONSULTING</div>
  <p class="service-copy">Lorem Ipsum is simply dummy text of the printing and typesetting industry Lorem Ipsum has.</p>
  <div class="btn">Read More</div>
</article>
<article class="service dark" style="left:369px">
  <div class="service-icon"><svg width="54" height="54" viewBox="0 0 54 54"><circle cx="27" cy="22" r="14" fill="var(--pill)"/><rect x="19" y="34" width="16" height="12" fill="var(--pill)"/><circle cx="27" cy="22" r="6" fill="none" stroke="#fff" stroke-width="2"/></svg></div>
  <div class="service-name">KNOWLEDGE<br>MANAGEMENT</div>
  <p class="service-copy">Lorem Ipsum is simply dummy text of the printing and typesetting industry Lorem Ipsum has.</p>
  <div class="btn">Read More</div>
</article>
<article class="service" style="left:606px">
  <div class="service-icon"><svg width="54" height="54" viewBox="0 0 54 54"><rect x="22" y="8" width="26" height="20" fill="none" stroke="var(--pill)" stroke-width="3"/><path d="M28 22l6-6 4 4 6-6" fill="none" stroke="var(--pill)" stroke-width="2"/><circle cx="12" cy="16" r="5" fill="var(--pill)"/><rect x="7" y="23" width="10" height="20" fill="var(--pill)"/><path d="M35 28l-6 16M35 28l6 16" stroke="var(--pill)" stroke-width="2"/></svg></div>
  <div class="service-name">TRAINING AND<br>ORGANISATIONAL<br>DEVELOPMENT</div>
  <p class="service-copy">Lorem Ipsum is simply dummy text of the printing and typesetting industry Lorem Ipsum has.</p>
  <div class="btn">Read More</div>
</article>
<article class="service" style="left:843px">
  <div class="service-icon"><svg width="58" height="54" viewBox="0 0 58 54"><circle cx="36" cy="20" r="12" fill="none" stroke="var(--pill)" stroke-width="7" stroke-dasharray="5 4"/><circle cx="36" cy="20" r="5" fill="var(--pill)"/><circle cx="18" cy="38" r="8" fill="none" stroke="var(--pill)" stroke-width="6" stroke-dasharray="4 3"/></svg></div>
  <div class="service-name">CONTACT CENTRE<br>OPTIMISATION</div>
  <p class="service-copy">Lorem Ipsum is simply dummy text of the printing and typesetting industry Lorem Ipsum has.</p>
  <div class="btn">Read More</div>
</article>

<!-- Welcome -->
<section class="welcome">
  <div class="welcome-photo" role="img" aria-label="Contact centre agents wearing headsets"></div>
  <div class="abs" style="left:436px;top:120px;width:118px;height:118px;border-radius:50%;background:var(--blue)"></div>
  <div class="abs" style="left:395px;top:252px;width:200px;text-align:center;font-size:18px;font-weight:600;color:var(--blue)">Harbor Lantern</div>
  <div class="welcome-kicker">WELCOME TO</div>
  <h2 class="welcome-title">HARBOR LANTERN</h2>
  <div class="welcome-rule"></div>
  <p class="welcome-copy">Everyone in the team at Harbor Lantern solutions have been accountable for delivering results within some of the most reputable Australian businesses. Our team are highly experienced practitioners.</p>
  <div class="btn" style="left:625px;top:321px;width:117px;height:38px;font-size:14.5px">Read More</div>
</section>

<!-- Vision -->
<section class="vision">
  <div class="vision-tag">OUR VISION</div>
  <p class="vision-text">ASIA PACIFIC'S MOST TRUSTED ADVISOR IN CUSTOMER EXPERIENCE AND SERVICE OPERATIONS</p>
</section>

<!-- Team -->
<h2 class="section-title" style="top:1866px">OUR TEAM</h2>
<div class="title-rule" style="top:1913px"></div>
<div class="team-arrow" style="left:76px"><svg width="8" height="12" viewBox="0 0 8 12"><path d="M6 1L1 6l5 5" fill="none" stroke="#888" stroke-width="1.5"/></svg></div>
<div class="team-arrow" style="left:1098px"><svg width="8" height="12" viewBox="0 0 8 12"><path d="M2 1l5 5-5 5" fill="none" stroke="#888" stroke-width="1.5"/></svg></div>

<article class="member" style="left:131px">
  <div class="member-photo" role="img" aria-label="Portrait of team member Marcus"></div>
  <div class="member-name">MARCUS</div><div class="member-role">Manager</div>
  <p class="member-copy">Lorem Ipsum is simply dummy text of the printing and typesetting indu.</p>
  <div class="btn">View Bio</div>
</article>
<article class="member" style="left:368px">
  <div class="member-photo" role="img" aria-label="Portrait of team member Daniel"></div>
  <div class="member-name">DANIEL</div><div class="member-role">Manager</div>
  <p class="member-copy">Lorem Ipsum is simply dummy text of the printing and typesetting indu.</p>
  <div class="btn">View Bio</div>
</article>
<article class="member" style="left:605px">
  <div class="member-photo" role="img" aria-label="Portrait of team member Tomas"></div>
  <div class="member-name">TOMAS</div><div class="member-role">Manager</div>
  <p class="member-copy">Lorem Ipsum is simply dummy text of the printing and typesetting indu.</p>
  <div class="btn">View Bio</div>
</article>
<article class="member" style="left:843px">
  <div class="member-photo" role="img" aria-label="Portrait of team member Adrian Vale"></div>
  <div class="member-name">ADRIAN VALE</div><div class="member-role">Manager</div>
  <p class="member-copy">Lorem Ipsum is simply dummy text of the printing and typesetting indu.</p>
  <div class="btn">View Bio</div>
</article>

<!-- Case studies -->
<section class="cases">
  <h2 class="section-title" style="top:40px">CASE STUDIES</h2>
  <div class="title-rule" style="top:90px"></div>
  <article class="case" style="left:131px">
    <div class="case-media" role="img" aria-label="Video still of an agent on a headset call"><div class="play"><svg width="16" height="18" viewBox="0 0 16 18"><path d="M2 1l13 8-13 8z" fill="var(--blue)"/></svg></div></div>
    <div class="case-title">LOREM IPSUM IS SIMPLY DUMMY TEXT OF THE PRINTING</div>
    <p class="case-copy">Lorem Ipsum is simply dummy text of the printing and typesetting indu.</p>
    <div class="btn">Read More</div>
  </article>
  <article class="case" style="left:453px">
    <div class="case-media" role="img" aria-label="Video still of an agent working in an office"><div class="play"><svg width="16" height="18" viewBox="0 0 16 18"><path d="M2 1l13 8-13 8z" fill="var(--blue)"/></svg></div></div>
    <div class="case-title">LOREM IPSUM IS SIMPLY DUMMY TEXT OF THE PRINTING</div>
    <p class="case-copy">Lorem Ipsum is simply dummy text of the printing and typesetting indu.</p>
    <div class="btn">Read More</div>
  </article>
  <article class="case" style="left:772px">
    <div class="case-media night" role="img" aria-label="Video still of hands holding a network of people icons"><div class="play"><svg width="16" height="18" viewBox="0 0 16 18"><path d="M2 1l13 8-13 8z" fill="var(--blue)"/></svg></div></div>
    <div class="case-title">LOREM IPSUM IS SIMPLY DUMMY TEXT OF THE PRINTING</div>
    <p class="case-copy">Lorem Ipsum is simply dummy text of the printing and typesetting indu.</p>
    <div class="btn">Read More</div>
  </article>
</section>

<!-- Newsletter -->
<section class="newsletter">
  <h2 class="news-title">NEWSLETTER SUBSCRIBE</h2>
  <p class="news-copy">Lorem Ipsum is simply dummy text of the printing and typesetting indu.</p>
  <div class="field" style="top:48px">Name</div>
  <div class="field" style="top:98px">E mail id</div>
  <div class="btn">Subscribe</div>
</section>

<!-- Footer -->
<footer class="footer">
  <div class="brand" style="left:131px;top:80px;font-size:34px;flex-direction:column;align-items:flex-start;gap:14px">
    <span class="brand-dot" style="width:70px;height:70px"></span>Harbor Lantern
  </div>

  <div class="foot-head" style="left:488px">MENU</div>
  <div class="foot-menu">HOME<br>ABOUT US<br>SERVICES<br>CASE STUDIES<br>CONTACT US</div>

  <div class="foot-head" style="left:700px">CONTACT US</div>
  <div class="foot-item" style="left:700px;top:86px"><span class="foot-icon"><svg width="8" height="11" viewBox="0 0 8 11"><path d="M4 0a4 4 0 014 4c0 3-4 7-4 7S0 7 0 4a4 4 0 014-4z" fill="var(--footer)"/></svg></span><span>ABN<br>12 345 678 901</span></div>
  <div class="foot-item" style="left:700px;top:138px"><span class="foot-icon"><svg width="10" height="10" viewBox="0 0 24 24"><path d="M6.6 10.8a15 15 0 006.6 6.6l2.2-2.2c.3-.3.7-.4 1-.2 1.1.4 2.3.6 3.6.6.6 0 1 .4 1 1V20c0 .6-.4 1-1 1A17 17 0 013 4c0-.6.4-1 1-1h3.5c.6 0 1 .4 1 1 0 1.3.2 2.5.6 3.6.1.3 0 .7-.2 1z" fill="var(--footer)"/></svg></span><span>Call Us<br>555.010.2040</span></div>
  <div class="foot-item" style="left:700px;top:190px"><span class="foot-icon"><svg width="10" height="8" viewBox="0 0 10 8"><rect width="10" height="8" fill="var(--footer)"/><path d="M0 0l5 4 5-4" fill="none" stroke="#fff"/></svg></span><span>E mail Us<br>info@harborlantern.com</span></div>

  <div class="foot-head" style="left:963px">FOLLOW US</div>
  <div class="foot-item" style="left:963px;top:86px"><span class="foot-icon"></span><span>Like us on<br>FACEPAGE</span></div>
  <div class="foot-item" style="left:963px;top:138px"><span class="foot-icon"></span><span>Follow us on<br>CHIRPER</span></div>
  <div class="foot-item" style="left:963px;top:190px"><span class="foot-icon"></span><span>Follow us on<br>LINKWORK</span></div>

  <div class="foot-rule"></div>
  <p class="copyright">Copyright © 2021 All Rights Reserved</p>
</footer>

</body>
</html>
```